Cool modern, tech Business card design

Looking for a new business card design for our Managed IT Services company. We would like 2 sides, with the logo one one side horizontally and then the information on the back in either vertical or horizontal. We want our colors from the logo incorporated but also would like to see the color gray in there as well.

Target Market(s)

IT, Information Technology, Tech, Service

Industry/Entity Type

It Service

Contact Information for Business Card

Carl Penner
Managing Partner
(P)555-271-4830 ext xxx
(F)555-271-4831
www.brixtelcore.com

Font styles to use
Sans Serif

Colors
959595
000000
ec1f27

Requirements
Must have
• Logo on one side with some nice design or pattern
• Information on back in either vertical or horizontal format
Nice to have
• For it to look cool, tech, modern, stand out.

```html
<!DOCTYPE html>
<html lang="en">
<head>
<meta charset="utf-8">
<title>Brixtelcore Business Card</title>
<link rel="stylesheet" href="https://fonts.googleapis.com/css2?family=Work+Sans:wght@400;500;600&display=swap">
<style>
  :root {
    --backdrop: #e7e2da;
    --card: #141414;
    --white: #ffffff;
    --red: #c8192e;
    --gray: #959595;
    --gray-dim: #343434;
  }
  * { margin: 0; padding: 0; box-sizing: border-box; }
  html, body { width: 1200px; height: 960px; overflow: hidden; }
  body {
    position: relative;
    background: var(--backdrop);
    font-family: "Work Sans", Arial, sans-serif;
    color: var(--white);
  }
  .card {
    position: absolute;
    top: 162px;
    width: 364px;
    height: 636px;
    background: var(--card);
    box-shadow: 2px 4px 8px rgba(0, 0, 0, 0.25);
    overflow: hidden;
  }
  .card--info { left: 221px; }
  .card--brand { left: 614px; }

  .accent-bar { position: absolute; width: 17px; }
  .accent-bar--white { background: var(--white); }
  .accent-bar--red { background: var(--red); }

  .card--info .accent-bar--white { left: 29px; top: 0; height: 238px; }
  .card--info .accent-bar--red { left: 29px; top: 305px; height: 331px; }
  .card--brand .accent-bar--white { left: 27px; top: 487px; height: 149px; }

  .circuit-pattern {
    position: absolute;
    left: 0;
    top: 108px;
    width: 364px;
    height: 180px;
  }
  .circuit-pattern__trace { stroke: var(--gray-dim); stroke-width: 14; stroke-linecap: round; fill: none; }
  .circuit-pattern__trace--light { stroke: var(--gray); stroke-opacity: 0.35; stroke-width: 4; }
  .circuit-pattern__node { fill: var(--gray); fill-opacity: 0.45; }

  .brand-name {
    position: absolute;
    display: flex;
    align-items: center;
    gap: 10px;
    font-weight: 500;
    color: var(--white);
    letter-spacing: -0.5px;
    white-space: nowrap;
  }
  .brand-name__mark {
    display: block;
    width: 14px;
    height: 14px;
    background: var(--red);
  }
  .card--info .brand-name { left: 72px; top: 198px; font-size: 31px; }
  .card--brand .brand-name { left: 68px; top: 562px; font-size: 34px; }

  .person { position: absolute; left: 73px; top: 304px; }
  .person__name { font-size: 32px; font-weight: 400; letter-spacing: 1px; line-height: 1; }
  .person__title { margin-top: 8px; font-size: 16.5px; letter-spacing: 0.6px; }

  .divider {
    position: absolute;
    left: 72px;
    top: 401px;
    width: 55px;
    height: 3px;
    background: var(--white);
  }

  .contact-list { position: absolute; left: 73px; top: 461px; list-style: none; }
  .contact-list__item {
    display: flex;
    align-items: center;
    height: 19px;
    margin-bottom: 11.5px;
    font-size: 16.5px;
    letter-spacing: 0.3px;
  }
  .contact-list__badge {
    width: 19px;
    height: 19px;
    margin-right: 16px;
    border-radius: 5px;
    background: var(--white);
    color: var(--card);
    font-size: 11px;
    font-weight: 500;
    display: flex;
    align-items: center;
    justify-content: center;
  }
</style>
</head>
<body>
  <section class="card card--info" aria-label="Business card, contact side">
    <span class="accent-bar accent-bar--white"></span>
    <div class="brand-name">brixtelcore<span class="brand-name__mark"></span></div>

    <span class="accent-bar accent-bar--red"></span>
    <div class="person">
      <h1 class="person__name">Carl Penner</h1>
      <p class="person__title">Managing Partner</p>
    </div>
    <span class="divider"></span>

    <ul class="contact-list">
      <li class="contact-list__item"><span class="contact-list__badge">T</span>555-271-4830</li>
      <li class="contact-list__item"><span class="contact-list__badge">F</span>555-271-4831</li>
      <li class="contact-list__item"><span class="contact-list__badge">W</span>www.brixtelcore.com</li>
    </ul>
  </section>

  <section class="card card--brand" aria-label="Business card, brand side">
    <svg class="circuit-pattern" viewBox="0 0 364 180" aria-hidden="true">
      <path class="circuit-pattern__trace" d="M-10 40 H120 L150 70 H250 L280 40 H380"/>
      <path class="circuit-pattern__trace" d="M-10 110 H70 L100 140 H200 L230 110 H380"/>
      <path class="circuit-pattern__trace circuit-pattern__trace--light" d="M20 165 H150 L170 145 H330"/>
      <path class="circuit-pattern__trace circuit-pattern__trace--light" d="M40 10 H180 L200 25 H340"/>
      <rect class="circuit-pattern__node" x="144" y="64" width="12" height="12" rx="2"/>
      <rect class="circuit-pattern__node" x="274" y="34" width="12" height="12" rx="2"/>
      <rect class="circuit-pattern__node" x="94" y="134" width="12" height="12" rx="2"/>
      <rect class="circuit-pattern__node" x="224" y="104" width="12" height="12" rx="2"/>
      <circle class="circuit-pattern__node" cx="330" cy="145" r="5"/>
      <circle class="circuit-pattern__node" cx="40" cy="10" r="5"/>
    </svg>
    <span class="accent-bar accent-bar--white"></span>
    <div class="brand-name">brixtelcore<span class="brand-name__mark"></span></div>
  </section>
</body>
</html>
```